BrovaLT BIZ Card, email signature & Stationary

Professional business cards, email signatures and ms word letterhead

Target Market(s)

business owners

Industry/Entity Type

cloud hosting

Contact Information for Business Card

name title office phone number , direct line, fax email address web site

Font styles to use
Other font styles liked:
• something that compliments font in logo

```html
<!DOCTYPE html>
<html lang="en">
<head>
<meta charset="utf-8">
<title>BrovaLT Stationery &amp; Email Signature</title>
<link href="https://fonts.googleapis.com/css2?family=Roboto:wght@300;400;500&display=swap" rel="stylesheet">
<style>
  :root{
    --red:#e31e26;
    --ink:#333336;
    --muted:#6b6b6e;
    --paper:#ffffff;
    --paper-soft:#f7f6f4;
    --card-grey:#ececeb;
    --stage:#e4e1dc;
    --frame:#cfcfcf;
  }
  *{margin:0;padding:0;box-sizing:border-box}
  html,body{width:1200px;height:641px;overflow:hidden;background:#fff}
  body{position:relative;font-family:"Roboto",Arial,sans-serif;color:var(--ink)}

  .wordmark{position:absolute;font-family:"Roboto",Arial,sans-serif;font-weight:300;color:var(--red);letter-spacing:-.02em;line-height:1;white-space:nowrap}
  .brand-dot{position:absolute;border-radius:50%;background:var(--ink)}

  .contacts{position:absolute;list-style:none;color:var(--ink);font-weight:400}
  .contacts li{display:flex;align-items:flex-start;line-height:1.1;white-space:nowrap}
  .contacts svg{flex:none;fill:var(--red)}
  .contacts.right li{flex-direction:row-reverse;text-align:right}
  .web{position:absolute;color:var(--red);white-space:nowrap;font-weight:400}

  /* email signature */
  .signature{position:absolute;left:53px;top:229px;width:320px;height:145px;background:var(--paper);border:1px solid var(--frame);box-shadow:1px 1px 2px rgba(0,0,0,.3);overflow:hidden}
  .signature .brand-dot{left:34px;top:52px;width:40px;height:40px}
  .signature .wordmark{left:94px;top:60px;font-size:24px}
  .person{position:absolute;left:199px;top:28px}
  .person .name{font-size:15px;font-weight:400;letter-spacing:.01em;line-height:1}
  .person .name b{font-weight:500}
  .person .role{font-size:7px;color:var(--muted);margin-top:1px}
  .signature .contacts{left:185px;top:58px;font-size:8px}
  .signature .contacts li{margin-bottom:5px}
  .signature .contacts li:last-child{margin-bottom:0}
  .signature .contacts svg{width:9px;height:9px;margin-right:5px;margin-top:1px}
  .signature .web{left:199px;top:120px;font-size:8px}
  .label{position:absolute;left:200px;top:405px;font-size:9px;color:#222b4a;letter-spacing:.02em}

  /* stationery set */
  .stage{position:absolute;left:418px;top:52px;width:720px;height:540px;background:var(--stage)}
  .sheet{position:absolute;background:var(--paper-soft);box-shadow:1px 2px 4px rgba(0,0,0,.12);overflow:hidden}

  .slip{left:224px;top:42px;width:121px;height:256px}
  .slip .wordmark{left:13px;top:34px;font-size:20px}
  .slip .contacts{left:15px;top:75px;font-size:5px}
  .slip .contacts li{margin-bottom:3px}
  .slip .contacts svg{width:5px;height:5px;margin-right:4px}
  .slip .brand-dot{left:14px;top:170px;width:44px;height:44px}
  .slip .web{left:48px;top:237px;font-size:5px}

  .letterhead{left:371px;top:136px;width:257px;height:362px}
  .letterhead .wordmark{left:32px;top:31px;font-size:18px}
  .letterhead .contacts{right:23px;top:32px;font-size:5px}
  .letterhead .contacts li{margin-bottom:3px}
  .letterhead .contacts svg{width:5px;height:5px;margin-left:4px}
  .letterhead .web{right:32px;top:335px;font-size:5px}

  .card-back{left:223px;top:322px;width:104px;height:67px;background:var(--card-grey)}
  .card-back .name{position:absolute;right:6px;top:44px;font-size:5.5px;line-height:1}
  .card-back .name b{font-weight:500}
  .card-back .role{position:absolute;right:6px;top:51px;font-size:3px;color:var(--muted)}

  .card-front{left:335px;top:322px;width:104px;height:67px;background:var(--paper)}
  .card-front .wordmark{right:6px;top:10px;font-size:14px}
  .card-front .contacts{left:7px;top:33px;font-size:3.3px}
  .card-front .contacts li{margin-bottom:2px}
  .card-front .contacts svg{width:3.5px;height:3.5px;margin-right:2px}
  .card-front .web{left:13px;top:58px;font-size:3px}

  .envelope{left:88px;top:415px;width:257px;height:125px}
  .envelope .wordmark{left:32px;top:32px;font-size:18px}
  .envelope .contacts{right:23px;top:33px;font-size:5px}
  .envelope .contacts li{margin-bottom:3px}
  .envelope .contacts svg{width:5px;height:5px;margin-left:4px}
</style>
</head>
<body>

<svg width="0" height="0" style="position:absolute" aria-hidden="true">
  <defs>
    <symbol id="icon-mail" viewBox="0 0 10 10"><rect x="0" y="2" width="10" height="6.4"/><path d="M.6 2.6 5 5.8l4.4-3.2" stroke="#fff" stroke-width=".9" fill="none"/></symbol>
    <symbol id="icon-phone" viewBox="0 0 10 10"><path d="M2.2 1 3.8 2.8 3 4c.7 1.4 1.6 2.3 3 3l1.2-.8L9 7.8 8 9C4.5 9 1 5.5 1 2z"/></symbol>
    <symbol id="icon-pin" viewBox="0 0 10 10"><path d="M5 0a3.4 3.4 0 0 0-3.4 3.4C1.6 6 5 10 5 10s3.4-4 3.4-6.6A3.4 3.4 0 0 0 5 0zm0 4.8a1.4 1.4 0 1 1 0-2.8 1.4 1.4 0 0 1 0 2.8z"/></symbol>
  </defs>
</svg>

<!-- Email signature -->
<section class="signature">
  <span class="brand-dot" aria-hidden="true"></span>
  <div class="wordmark">BrovaLT</div>
  <div class="person">
    <p class="name"><b>JOHN</b> DOE</p>
    <p class="role">Lorem ipsum dolor</p>
  </div>
  <ul class="contacts">
    <li><svg><use href="#icon-mail"/></svg><span>loremipsum@lorem.com</span></li>
    <li><svg><use href="#icon-phone"/></svg><span>+00 1234 5678 90</span></li>
    <li><svg style="margin-top:6px"><use href="#icon-pin"/></svg><span>Lorem ipsum dolor sit amet<br>consectetur adipiscing elit<br>consectetur adipiscing elit</span></li>
  </ul>
  <p class="web">www.websiteaddress.com</p>
</section>
<p class="label">EMAIL</p>

<!-- Stationery set -->
<section class="stage">
  <article class="sheet slip">
    <div class="wordmark">BrovaLT</div>
    <ul class="contacts">
      <li><svg><use href="#icon-mail"/></svg><span>loremipsum@lorem.com</span></li>
      <li><svg><use href="#icon-phone"/></svg><span>+00 1234 5678 90</span></li>
      <li><svg style="margin-top:3px"><use href="#icon-pin"/></svg><span>Lorem ipsum dolor sit amet<br>consectetur adipiscing elit<br>consectetur adipiscing elit</span></li>
    </ul>
    <span class="brand-dot" aria-hidden="true"></span>
    <p class="web">www.websiteaddress.com</p>
  </article>

  <article class="sheet letterhead">
    <div class="wordmark">BrovaLT</div>
    <ul class="contacts right">
      <li><svg><use href="#icon-mail"/></svg><span>loremipsum@lorem.com</span></li>
      <li><svg><use href="#icon-phone"/></svg><span>+00 1234 5678 90</span></li>
      <li><svg style="margin-top:3px"><use href="#icon-pin"/></svg><span>Lorem ipsum dolor sit amet<br>consectetur adipiscing elit<br>consectetur adipiscing elit</span></li>
    </ul>
    <p class="web">www.websiteaddress.com</p>
  </article>

  <article class="sheet card-back">
    <p class="name"><b>JOHN</b> DOE</p>
    <p class="role">Lorem ipsum dolor</p>
  </article>

  <article class="sheet card-front">
    <div class="wordmark">BrovaLT</div>
    <ul class="contacts">
      <li><svg><use href="#icon-mail"/></svg><span>loremipsum@lorem.com</span></li>
      <li><svg><use href="#icon-phone"/></svg><span>+00 1234 5678 90</span></li>
      <li><svg style="margin-top:2px"><use href="#icon-pin"/></svg><span>Lorem ipsum dolor sit amet<br>consectetur adipiscing elit<br>consectetur adipiscing elit</span></li>
    </ul>
    <p class="web">www.websiteaddress.com</p>
  </article>

  <article class="sheet envelope">
    <div class="wordmark">BrovaLT</div>
    <ul class="contacts right">
      <li><svg><use href="#icon-mail"/></svg><span>loremipsum@lorem.com</span></li>
      <li><svg><use href="#icon-phone"/></svg><span>+00 1234 5678 90</span></li>
      <li><svg style="margin-top:3px"><use href="#icon-pin"/></svg><span>Lorem ipsum dolor sit amet<br>consectetur adipiscing elit<br>consectetur adipiscing elit</span></li>
    </ul>
  </article>
</section>

</body>
</html>
```